Powerpoint template for Marlowe Stewardship Partners

I would like to use my logo and colors to create a powerpoint deck that I can use for various presentations. I would want the design to be modern, use my logo on each page (small at the bottom by the slide number) and have a couple of transition slides for cover page, transition page, etc.

```html
<!DOCTYPE html>
<html lang="en">
<head>
<meta charset="utf-8">
<title>Marlowe Stewardship Partners – Presentation Template</title>
<link href="https://fonts.googleapis.com/css2?family=Poppins:ital,wght@0,400;0,500;0,600;0,700;1,400&display=swap" rel="stylesheet">
<style>
  :root{
    --bg:#dcdedc;
    --blue:#2b62ea;
    --blue-2:#4a7ff2;
    --ink:#1c1e2a;
    --muted:#a0a3ad;
    --white:#ffffff;
    --line:#e6e8ee;
    --accent:#8a3ccf;
  }
  *{box-sizing:border-box;margin:0;padding:0}
  html,body{width:1200px;height:2810px;overflow:hidden}
  body{background:var(--bg);font-family:"Poppins",sans-serif;color:var(--ink);position:relative}
  .deck{position:absolute;left:96px;top:68px;display:grid;grid-template-columns:503px 503px;grid-auto-rows:282px;gap:12px}
  .slide{position:relative;background:var(--white);overflow:hidden;box-shadow:0 4px 14px rgba(0,0,0,.12)}
  .slide.blue{background:linear-gradient(120deg,var(--blue) 0%,var(--blue-2) 100%);color:var(--white)}
  .abs{position:absolute}
  .hd{position:absolute;top:29px;font-size:5px;font-weight:600;color:var(--ink)}
  .blue .hd,.on-blue{color:var(--white)}
  .ft{position:absolute;right:14px;bottom:10px;display:flex;align-items:center;gap:12px;font-size:6px;color:var(--blue)}
  .ft .brand{font-weight:600;letter-spacing:.3px;border-bottom:1px solid currentColor;padding-bottom:1px}
  .ft .num{color:var(--muted);font-size:6.5px}
  .blue .ft,.ft.light{color:var(--white)}
  .blue .ft .num,.ft.light .num{color:var(--white)}
  .t{position:absolute;font-size:16px;font-weight:500;line-height:1.2;color:var(--ink)}
  .t b{font-weight:600;color:var(--blue)}
  .p{position:absolute;font-size:5.3px;line-height:1.85;color:var(--muted)}
  .lbl{position:absolute;font-size:5.6px;font-weight:600;color:var(--ink)}
  .btn{position:absolute;height:19px;border-radius:10px;background:var(--blue);color:var(--white);font-size:5.5px;display:flex;align-items:center;justify-content:space-between;padding:0 4px 0 11px;gap:8px}
  .btn.light{background:var(--white);color:var(--blue)}
  .btn svg{width:11px;height:11px}
  .ico{width:10px;height:10px;display:inline-block;vertical-align:middle}
  .photo{position:absolute;background:linear-gradient(135deg,#8a96a8,#cfd5dd)}
  .photo.office{background:linear-gradient(135deg,#6f6a66,#c7bfb6 55%,#e8e3dc)}
  .photo.city{background:linear-gradient(180deg,#c9d7e6,#7d91a8 60%,#d8dde3)}
  .photo.sky{background:linear-gradient(160deg,#4d8fd6,#a8c9ec 45%,#6f7785)}
  .photo.warm{background:linear-gradient(135deg,#c9a189,#e9d6c8 50%,#8a8f99)}
  .photo.tint{background:linear-gradient(120deg,rgba(255,255,255,.06),rgba(20,40,120,.18))}
  .card{position:absolute;border-radius:4px}
  .card.blue-c{background:var(--blue);color:var(--white)}
  .card.white-c{background:var(--white);box-shadow:0 3px 12px rgba(0,0,0,.12)}
  .big{font-weight:600;color:var(--blue)}
  .list-row{position:absolute;display:flex;align-items:center;gap:6px;font-size:5.6px;font-weight:600}
</style>
</head>
<body>
<svg width="0" height="0" style="position:absolute" aria-hidden="true">
  <symbol id="tick" viewBox="0 0 10 10"><circle cx="5" cy="5" r="5" fill="#2b62ea"/><path d="M2.8 5.1l1.5 1.5 3-3.1" fill="none" stroke="#fff" stroke-width="1.2" stroke-linecap="round" stroke-linejoin="round"/></symbol>
  <symbol id="tick-w" viewBox="0 0 10 10"><circle cx="5" cy="5" r="5" fill="#fff"/><path d="M2.8 5.1l1.5 1.5 3-3.1" fill="none" stroke="#2b62ea" stroke-width="1.2" stroke-linecap="round" stroke-linejoin="round"/></symbol>
  <symbol id="go" viewBox="0 0 12 12"><circle cx="6" cy="6" r="6" fill="#fff"/><path d="M5 3.8l2.2 2.2L5 8.2" fill="none" stroke="#2b62ea" stroke-width="1.3" stroke-linecap="round" stroke-linejoin="round"/></symbol>
  <symbol id="go-b" viewBox="0 0 12 12"><circle cx="6" cy="6" r="6" fill="#2b62ea"/><path d="M5 3.8l2.2 2.2L5 8.2" fill="none" stroke="#fff" stroke-width="1.3" stroke-linecap="round" stroke-linejoin="round"/></symbol>
  <symbol id="dot-icon" viewBox="0 0 14 14"><circle cx="7" cy="7" r="7" fill="currentColor"/><rect x="4.5" y="4.5" width="5" height="5" rx="1" fill="none" stroke="#fff" stroke-width="1.1"/></symbol>
</svg>

<main class="deck">

  <!-- 1 Cover -->
  <section class="slide">
    <div class="abs" style="left:0;right:0;top:118px;text-align:center;font-size:30px;font-weight:500;line-height:1.1;color:var(--blue)">Marlowe<br>Stewardship Partners</div>
  </section>

  <!-- 2 Title -->
  <section class="slide blue">
    <div class="photo tint" role="img" aria-label="Business team meeting around a table" style="inset:0"></div>
    <div class="abs on-blue" style="left:41px;top:48px;font-size:12px;font-weight:500">Marlowe Stewardship Partners</div>
    <div class="t on-blue" style="left:41px;top:92px;font-size:29px;font-weight:600;line-height:1.15">Marlowe Stewardship<br>Partners</div>
    <div class="abs on-blue" style="left:41px;top:179px;font-size:8.5px;font-weight:600">Business Presentation Template</div>
    <div class="p on-blue" style="left:41px;top:222px;width:220px;color:#fff">Lorem ipsum dolor sit amet, consectetuer adipiscing elit. Maecenas porttitor congue massa. Fusce posuere, magna sed pulvinar.</div>
    <div class="btn light" style="left:384px;top:221px;width:74px">Learn More <svg><use href="#go-b"/></svg></div>
  </section>

  <!-- 3 Welcome -->
  <section class="slide">
    <div class="hd" style="left:25px">Marlowe Stewardship Partners</div>
    <div class="hd" style="left:369px">Business Company</div>
    <div class="hd" style="left:464px">2026</div>
    <div class="t" style="left:43px;top:70px">Welcome To<br><b>Marlowe Stewardship<br>Partners</b></div>
    <div class="lbl" style="left:43px;top:143px">Best Description Here</div>
    <div class="p" style="left:43px;top:154px;width:170px">Lorem ipsum dolor sit amet, consectetuer adipiscing elit. Maecenas porttitor congue massa. Fusce posuere, magna sed pulvinar ultricies, purus lobortis libero.</div>
    <div class="list-row" style="left:43px;top:198px"><svg class="ico"><use href="#tick"/></svg>Option Number One</div>
    <div class="p" style="left:43px;top:212px;width:140px">Lorem ipsum dolor sit amet, consectetur adipiscing elit, sed do eiusmod tempor.</div>
    <div class="photo warm" role="img" aria-label="Colleagues reviewing charts on a desk" style="left:251px;top:65px;right:0;height:183px;border-radius:6px 0 0 6px"></div>
    <div class="ft"><span class="brand">MARLOWE</span><span class="num">3</span></div>
  </section>

  <!-- 4 About -->
  <section class="slide">
    <div class="hd" style="left:25px">Marlowe Stewardship Partners</div>
    <div class="hd" style="left:369px">Business Company</div>
    <div class="hd" style="left:464px">2026</div>
    <div class="abs" style="left:44px;top:82px;width:130px;height:118px;background:var(--blue);border-radius:6px"></div>
    <div class="photo city" role="img" aria-label="City skyline across the water" style="left:58px;top:69px;width:196px;height:120px;border-radius:6px"></div>
    <div class="t" style="left:282px;top:75px">About Marlowe<br><b>Stewardship Partners</b></div>
    <div class="p" style="left:282px;top:128px;width:176px;text-align:justify">Marlowe Stewardship Partners was founded in 2025 by Dana Whitcombe, a seasoned executive with over 30 years of experience in fleet management. Her career spans from assistant to chief client officer at a large enterprise, bringing deep expertise in leadership, mentorship and strategy.</div>
    <div class="p" style="left:282px;top:200px;font-style:italic;font-weight:600">Nunc viverra imperdiet enim. Fusce est. Vivamus a tellus.</div>
    <div class="lbl" style="left:44px;top:218px">Description</div>
    <div class="p" style="left:44px;top:228px;width:112px">Lorem ipsum is simply dummy text for example simply dummy text for</div>
    <div class="abs big" style="left:180px;top:228px;font-size:17px">60%</div>
    <div class="lbl" style="left:282px;top:218px">Description</div>
    <div class="p" style="left:282px;top:228px;width:112px">Lorem ipsum is simply dummy text for example simply dummy text for</div>
    <div class="abs big" style="left:421px;top:228px;font-size:17px">89k</div>
    <div class="ft"><span class="brand">MARLOWE</span><span class="num">4</span></div>
  </section>

  <!-- 5 Mission -->
  <section class="slide">
    <div class="hd" style="left:25px">Marlowe Stewardship Partners</div>
    <div class="hd" style="left:369px">Business Company</div>
    <div class="hd" style="left:464px">2026</div>
    <div class="photo city" role="img" aria-label="Handshake over a city backdrop" style="left:44px;top:52px;width:179px;height:85px;border-radius:6px"></div>
    <div class="photo office" role="img" aria-label="Team working together at a laptop" style="left:44px;top:152px;width:179px;height:85px;border-radius:6px"></div>
    <div class="t" style="left:281px;top:70px">3. Mission &amp;<br><b>Purpose</b></div>
    <div class="p" style="left:281px;top:120px;width:180px">Lorem ipsum dolor sit amet, consectetuer adipiscing elit. Maecenas porttitor congue massa posuere.</div>
    <div class="list-row" style="left:281px;top:160px"><svg class="ico"><use href="#tick"/></svg>Description</div>
    <div class="p" style="left:281px;top:172px;width:90px">Lorem ipsum dolor sit amet, consectetur adipiscing elit</div>
    <div class="list-row" style="left:385px;top:160px"><svg class="ico"><use href="#tick"/></svg>Description</div>
    <div class="p" style="left:385px;top:172px;width:90px">Lorem ipsum dolor sit amet, consectetur adipiscing elit</div>
    <div class="btn" style="left:281px;top:208px;width:74px">Learn More <svg><use href="#go"/></svg></div>
    <div class="ft"><span class="brand">MARLOWE</span><span class="num">5</span></div>
  </section>

  <!-- 6 What We Do -->
  <section class="slide">
    <div class="photo office" role="img" aria-label="Team meeting in a bright office" style="left:0;top:0;width:222px;height:100%"></div>
    <div class="hd on-blue" style="left:25px">Marlowe Stewardship Partners</div>
    <div class="hd" style="left:369px">Business Company</div>
    <div class="hd" style="left:464px">2026</div>
    <div class="t" style="left:281px;top:52px">What <b>We Do</b></div>
    <div class="p" style="left:281px;top:76px;width:178px;text-align:justify">Lorem ipsum dolor sit amet, consectetuer adipiscing elit. Maecenas porttitor congue massa. Fusce posuere, magna sed pulvinar ultricies, purus lectus malesuada libero, sit amet commodo.</div>
    <div class="card blue-c" style="left:189px;top:131px;width:275px;height:50px;border-radius:3px">
      <div class="abs" style="left:31px;top:17px;font-size:5.8px;font-weight:600;line-height:1.9">Build Succes with<br>Our growth business</div>
      <div class="abs" style="left:133px;top:18px;width:130px;font-size:5.3px;line-height:1.85">Lorem ipsum dolor sit amet, consectetuer adipiscing elit. Maecenas porttitor e massa</div>
    </div>
    <div class="p" style="left:281px;top:200px;width:178px;text-align:justify">Lorem ipsum dolor sit amet, consectetuer adipiscing elit. Maecenas porttitor congue massa. Fusce posuere, magna sed pulvinar ultricies, purus lectus malesuada libero, sit amet commodo.</div>
    <div class="ft"><span class="brand">MARLOWE</span><span class="num">6</span></div>
  </section>

  <!-- 7 Coaching -->
  <section class="slide">
    <div class="photo warm" role="img" aria-label="Executive holding documents in a boardroom" style="left:0;top:0;width:242px;height:100%;border-radius:0 0 26px 0"></div>
    <div class="hd" style="left:369px">Business Company</div>
    <div class="hd" style="left:464px">2026</div>
    <div class="t" style="left:279px;top:54px">Executive <b>Leadership<br>Coaching</b></div>
    <div class="abs" style="left:279px;top:114px;width:4px;height:4px;border-radius:50%;background:var(--blue)"></div>
    <div class="lbl" style="left:293px;top:112px">Vision 01</div>
    <div class="p" style="left:293px;top:123px;width:150px">Lorem ipsum dolor sit amet dolor sit amet dolor sit amet dolor sit amet, adipis cing ipsum dolor</div>
    <div class="abs" style="left:279px;top:164px;width:4px;height:4px;border-radius:50%;background:var(--blue)"></div>
    <div class="lbl" style="left:293px;top:162px">Vision 02</div>
    <div class="p" style="left:293px;top:173px;width:150px">Lorem ipsum dolor sit amet dolor sit amet dolor sit amet dolor sit amet, adipis cing ipsum dolor</div>
    <div class="abs" style="left:279px;top:214px;width:4px;height:4px;border-radius:50%;background:var(--blue)"></div>
    <div class="lbl" style="left:293px;top:212px">Vision 03</div>
    <div class="p" style="left:293px;top:223px;width:150px">Lorem ipsum dolor sit amet dolor sit amet dolor sit amet dolor sit amet, adipis cing ipsum dolor</div>
    <div class="ft"><span class="brand">MARLOWE</span><span class="num">7</span></div>
  </section>

  <!-- 8 Relationship -->
  <section class="slide">
    <div class="hd" style="left:25px">Marlowe Stewardship Partners</div>
    <div class="hd" style="left:369px">Business Company</div>
    <div class="hd" style="left:464px">2026</div>
    <div class="abs" style="left:117px;top:51px;width:118px;height:163px;background:var(--blue);border-radius:8px"></div>
    <div class="photo office" role="img" aria-label="Business partners shaking hands at a desk" style="left:45px;top:69px;width:168px;height:213px;border-radius:6px 6px 0 0"></div>
    <div class="t" style="left:280px;top:76px">Relationship<br><b>Management</b></div>
    <div class="p" style="left:280px;top:130px;width:180px;text-align:justify">Lorem ipsum dolor sit amet, consectetuer adipiscing elit. Maecenas porttitor congue massa. Fusce posuere, magna sed pulvinar ultricies, purus lectus posuere, magna porttitor.</div>
    <svg class="abs" style="left:280px;top:196px;width:15px;height:15px;color:var(--blue)"><use href="#dot-icon"/></svg>
    <div class="lbl" style="left:307px;top:196px">Best Description Here</div>
    <div class="p" style="left:307px;top:207px;width:153px;text-align:justify">Lorem ipsum dolor sit amet, consectetuer adipiscing elit. Maecenas porttitor. Fusce posuere, magna porttitor massa. Fusce posuere, magna porttitor.</div>
    <div class="ft"><span class="brand">MARLOWE</span><span class="num">8</span></div>
  </section>

  <!-- 9 Break -->
  <section class="slide blue">
    <div class="photo tint" role="img" aria-label="Office towers under a blue overlay" style="inset:0"></div>
    <div class="hd" style="left:25px">Marlowe Stewardship Partners</div>
    <div class="hd" style="left:369px">Business Company</div>
    <div class="hd" style="left:464px">2026</div>
    <div class="t on-blue" style="left:42px;top:170px;font-size:40px;font-weight:600">Breakslide</div>
    <div class="abs on-blue" style="left:43px;top:219px;font-size:12px;font-weight:500">Take Short A Break</div>
    <div class="ft"><span class="brand">MARLOWE</span><span class="num">9</span></div>
  </section>

  <!-- 10 Strategic Growth -->
  <section class="slide">
    <div class="hd" style="left:25px">Marlowe Stewardship Partners</div>
    <div class="photo sky" role="img" aria-label="Looking up at glass skyscrapers against the sky" style="left:221px;top:0;right:0;height:153px;border-radius:0 0 0 24px"></div>
    <div class="t" style="left:44px;top:58px">Strategic Growth<br><b>Planning</b></div>
    <div class="p" style="left:44px;top:106px;width:140px;text-align:justify">Lorem ipsum dolor sit amet, consectetuer adipiscing elit. Maecenas porttitor massa. Fusce posuere, magna porttitor. Fusce posuere, magna sed pulvinar ultricies, posuere magna porttitor.</div>
    <svg class="abs" style="left:44px;top:186px;width:16px;height:16px;color:var(--blue)"><use href="#dot-icon"/></svg>
    <svg class="abs" style="left:150px;top:186px;width:16px;height:16px;color:#3a3d46"><use href="#dot-icon"/></svg>
    <svg class="abs" style="left:256px;top:186px;width:16px;height:16px;color:var(--blue)"><use href="#dot-icon"/></svg>
    <svg class="abs" style="left:362px;top:186px;width:16px;height:16px;color:#3a3d46"><use href="#dot-icon"/></svg>
    <div class="lbl" style="left:44px;top:213px">Business Planning</div>
    <div class="lbl" style="left:150px;top:213px">Market Research</div>
    <div class="lbl" style="left:256px;top:213px">Chart Management</div>
    <div class="lbl" style="left:362px;top:213px">Program Management</div>
    <div class="p" style="left:44px;top:223px;width:92px">Lorem ipsum dolor sit amet, consectetuer adipiscing elit.</div>
    <div class="p" style="left:150px;top:223px;width:92px">Lorem ipsum dolor sit amet, consectetuer adipiscing elit.</div>
    <div class="p" style="left:256px;top:223px;width:92px">Lorem ipsum dolor sit amet, consectetuer adipiscing elit.</div>
    <div class="p" style="left:362px;top:223px;width:92px">Lorem ipsum dolor sit amet, consectetuer adipiscing elit.</div>
    <div class="ft"><span class="brand">MARLOWE</span><span class="num">10</span></div>
  </section>

  <!-- 11 Why -->
  <section class="slide">
    <div class="abs" style="left:340px;top:0;right:0;bottom:0;background:var(--blue)"></div>
    <div class="hd" style="left:25px">Marlowe Stewardship Partners</div>
    <div class="hd on-blue" style="left:369px">Business Company</div>
    <div class="hd on-blue" style="left:464px">2026</div>
    <div class="t" style="left:43px;top:78px">Why Marlowe<br><b>Stewardship<br>Partners</b></div>
    <div class="p" style="left:43px;top:154px;width:165px;text-align:justify">Lorem ipsum dolor sit amet, consectetuer adipiscing elit. Maecenas porttitor congue massa. Fusce posuere, magna sed pulvinar ultricies, purus lectus malesuada libero, sit amet commodo.</div>
    <div class="btn" style="left:43px;top:215px;width:90px">Get Started Now <svg><use href="#go"/></svg></div>
    <div class="photo office" role="img" aria-label="Professional working on a laptop in an office" style="left:252px;top:52px;width:201px;height:201px;border-radius:8px"></div>
    <div class="ft light"><span class="brand">MARLOWE</span><span class="num">11</span></div>
  </section>

  <!-- 12 Client Analytic -->
  <section class="slide">
    <div class="hd" style="left:25px">Marlowe Stewardship Partners</div>
    <div class="hd" style="left:369px">Business Company</div>
    <div class="hd" style="left:464px">2026</div>
    <div class="t" style="left:44px;top:78px">Our Client Global Analytic<br><b>Marlowe Stewardship<br>Partners</b></div>
    <div class="p" style="left:309px;top:78px;width:150px;text-align:justify">Lorem ipsum dolor sit amet, consectetuer adipiscing elit. Maecenas porttitor congue massa. Fusce posuere, magna sed pulvinar ultricies, purus lectus malesuada libero, sit amet commodo.</div>
    <div class="photo city" role="img" aria-label="Handshake over a city skyline" style="left:44px;top:153px;width:207px;height:129px;border-radius:6px 6px 0 0"></div>
    <div class="card blue-c" style="left:203px;top:169px;width:258px;height:66px">
      <div class="abs" style="left:22px;top:17px;font-size:26px;font-weight:500;line-height:1.2">50K</div>
      <div class="abs" style="left:112px;top:18px;font-size:5.6px;font-weight:600">Description</div>
      <div class="abs" style="left:112px;top:29px;width:130px;font-size:5.3px;line-height:1.85">Lorem ipsum dolor sit amet, consectetuer adipiscing elit. Maecenas porttitor e massa</div>
    </div>
    <div class="ft"><span class="brand">MARLOWE</span><span class="num">12</span></div>
  </section>

  <!-- 13 Service -->
  <section class="slide">
    <div class="hd" style="left:25px">Marlowe Stewardship Partners</div>
    <div class="hd" style="left:369px">Business Company</div>
    <div class="hd" style="left:464px">2026</div>
    <div class="t" style="left:43px;top:78px">Service &amp; <b>Features</b></div>
    <div class="p" style="left:43px;top:105px;width:180px;text-align:justify">Lorem ipsum dolor sit amet, consectetuer adipiscing elit. Maecenas porttitor congue massa. Fusce posuere, magna sed pulvinar ultricies, purus libero, sit amet commodo.</div>
    <div class="list-row" style="left:251px;top:101px"><svg class="ico"><use href="#tick"/></svg>Description</div>
    <div class="p" style="left:251px;top:114px;width:90px">Lorem ipsum dolor sit amet, consectetur adipiscing elit</div>
    <div class="list-row" style="left:365px;top:101px"><svg class="ico"><use href="#tick"/></svg>Description</div>
    <div class="p" style="left:365px;top:114px;width:90px">Lorem ipsum dolor sit amet, consectetur adipiscing elit</div>
    <div class="photo" role="img" aria-label="Hands typing on a laptop showing dashboards" style="left:43px;top:160px;width:210px;height:91px;border-radius:4px;background:linear-gradient(135deg,#3a3f4a,#d9dde3 60%,#f2f3f5)"></div>
    <div class="card blue-c" style="left:263px;top:160px;width:94px;height:91px;text-align:center">
      <svg style="position:absolute;left:33px;top:14px;width:28px;height:28px" viewBox="0 0 28 28"><path d="M14 2a12 12 0 1 0 12 12H14z" fill="#fff"/><path d="M16 0v12h12A12 12 0 0 0 16 0z" fill="#fff"/></svg>
      <div class="abs" style="left:0;right:0;top:50px;font-size:16px;font-weight:500">578K</div>
      <div class="abs" style="left:0;right:0;top:71px;font-size:6px;font-weight:600">Description</div>
    </div>
    <div class="card white-c" style="left:365px;top:160px;width:94px;height:91px;text-align:center">
      <svg style="position:absolute;left:35px;top:14px;width:24px;height:26px" viewBox="0 0 24 26"><rect x="8" y="0" width="8" height="7" fill="#2b62ea"/><path d="M12 7v5M4 12h16M4 12v4M12 12v4M20 12v4" stroke="#2b62ea" stroke-width="1.5" fill="none"/><rect x="0" y="16" width="8" height="7" fill="#2b62ea"/><rect x="8" y="16" width="8" height="7" fill="#2b62ea"/><rect x="16" y="16" width="8" height="7" fill="#2b62ea"/></svg>
      <div class="abs" style="left:0;right:0;top:50px;font-size:16px;font-weight:500;color:var(--ink)">40M</div>
      <div class="abs" style="left:0;right:0;top:71px;font-size:6px;font-weight:600;color:var(--ink)">Description</div>
    </div>
    <div class="ft"><span class="brand">MARLOWE</span><span class="num">13</span></div>
  </section>

  <!-- 14 Consultation -->
  <section class="slide">
    <div class="hd" style="left:25px">Marlowe Stewardship Partners</div>
    <div class="photo" role="img" aria-label="Consultant pointing at printed charts" style="left:265px;top:52px;width:194px;height:202px;border-radius:6px;background:linear-gradient(160deg,#eef1f5,#cfd8e3 55%,#9aa6b5)"></div>
    <div class="t" style="left:43px;top:78px">Come In For A Free<br><b>Consultation</b></div>
    <div class="card white-c" style="left:43px;top:142px;width:63px;height:78px;text-align:center">
      <div class="abs" style="left:0;right:0;top:13px;font-size:18px;font-weight:500">70%</div>
      <div class="abs" style="left:0;right:0;top:39px;font-size:5.8px;font-weight:600">Description</div>
      <div class="abs" style="left:8px;right:8px;top:50px;font-size:5px;line-height:1.8;color:var(--muted)">Lorem ipsum dolor sit amet, consectetur</div>
    </div>
    <div class="card blue-c" style="left:156px;top:142px;width:225px;height:80px">
      <svg style="position:absolute;left:18px;top:23px;width:34px;height:34px" viewBox="0 0 34 34"><rect x="12" y="0" width="10" height="9" rx="1" fill="#fff"/><path d="M17 9v6M5 15h24M5 15v6M17 15v6M29 15v6" stroke="#fff" stroke-width="2" fill="none"/><rect x="0" y="21" width="10" height="9" rx="1" fill="#fff"/><rect x="12" y="21" width="10" height="9" rx="1" fill="#fff"/><rect x="24" y="21" width="10" height="9" rx="1" fill="#fff"/></svg>
      <div class="abs" style="left:80px;top:14px;font-size:19px;font-weight:500">108K</div>
      <div class="abs" style="left:80px;top:43px;width:130px;font-size:5.3px;line-height:1.85">Lorem ipsum dolor sit amet, consectetuer adipiscing elit. Maecenas porttitor e massa</div>
    </div>
    <div class="lbl" style="left:43px;top:240px">Lorem ipsum dolor sit amet, consectetur adipisicing elit</div>
    <div class="ft"><span class="brand">MARLOWE</span><span class="num">14</span></div>
  </section>

  <!-- 15 Solution -->
  <section class="slide">
    <div class="abs" style="left:0;top:0;width:260px;bottom:0;background:var(--blue)"></div>
    <div class="hd on-blue" style="left:25px">Marlowe Stewardship Partners</div>
    <div class="hd" style="left:369px">Business Company</div>
    <div class="hd" style="left:464px">2026</div>
    <div class="t on-blue" style="left:43px;top:70px">Get The Perfect<br>Solution For Your<br>Business</div>
    <div class="list-row on-blue" style="left:43px;top:152px"><svg class="ico"><use href="#tick-w"/></svg>Real Time Collaboration</div>
    <div class="list-row on-blue" style="left:43px;top:172px"><svg class="ico"><use href="#tick-w"/></svg>Connect with your team members</div>
    <div class="list-row on-blue" style="left:43px;top:192px"><svg class="ico"><use href="#tick-w"/></svg>Easy Send Payment</div>
    <div class="btn light" style="left:43px;top:236px;width:74px">Learn More <svg><use href="#go-b"/></svg></div>
    <div class="p" style="left:292px;top:80px;width:168px;text-align:justify">Lorem ipsum dolor sit amet, consectetuer adipiscing elit. Maecenas porttitor congue massa. Fusce posuere, magna sed pulvinar ultricies, purus lectus malesuada libero, sit amet commodo.</div>
    <div class="photo warm" role="img" aria-label="Team gathered around a wall of sticky notes" style="left:207px;top:142px;width:225px;height:140px;border-radius:6px 6px 0 0"></div>
    <div class="card blue-c" style="left:403px;top:194px;width:74px;height:60px;text-align:center">
      <div class="abs" style="left:0;right:0;top:10px;font-size:18px;font-weight:500">70%</div>
      <div class="abs" style="left:0;right:0;top:36px;font-size:6px;font-weight:600">Description</div>
    </div>
    <div class="ft"><span class="brand">MARLOWE</span><span class="num">15</span></div>
  </section>

  <!-- 16 Team -->
  <section class="slide">
    <div class="hd" style="left:25px">Marlowe Stewardship Partners</div>
    <div class="hd" style="left:369px">Business Company</div>
    <div class="hd" style="left:464px">2026</div>
    <div class="t" style="left:43px;top:78px">Grow Our Team<br><b>Faster With Us</b></div>
    <div class="p" style="left:43px;top:124px;width:175px;text-align:justify">Lorem ipsum dolor sit amet, consectetuer adipiscing elit. Maecenas porttitor congue massa. Fusce posuere, magna sed pulvinar ultricies, purus lectus malesuada libero, sit amet commodo magna eros quis urna.</div>
    <div class="p" style="left:43px;top:180px;width:175px">Nunc viverra imperdiet enim. Fusce est. Vivamus a tellus.</div>
    <div class="btn" style="left:43px;top:216px;width:74px">Learn More <svg><use href="#go"/></svg></div>
    <div class="card white-c" style="left:260px;top:63px;width:216px;height:76px;border-radius:4px;border-right:2px solid var(--accent)">
      <div class="photo" role="img" aria-label="Portrait of the founder" style="left:2px;top:5px;width:74px;height:66px;border-radius:3px;background:linear-gradient(160deg,#e7e2dc,#b9b1a8)"></div>
      <div class="abs" style="left:90px;top:12px;font-size:8.5px;font-weight:600">Dana Whitcombe</div>
      <div class="abs" style="left:90px;top:25px;font-size:5.5px;font-weight:600">The Founder</div>
      <div class="abs" style="left:90px;top:40px;width:105px;font-size:5.3px;line-height:1.85;color:var(--muted);text-align:justify">Lorem ipsum dolor sit amet, consectetur adipiscing elit</div>
    </div>
    <div class="card blue-c" style="left:252px;top:169px;width:225px;height:78px">
      <div class="photo" role="img" aria-label="Portrait of the general manager" style="left:10px;top:6px;width:74px;height:66px;border-radius:3px;background:linear-gradient(160deg,#dfe3ea,#8d96a6)"></div>
      <div class="abs" style="left:98px;top:13px;font-size:8.5px;font-weight:600">Ravi Okafor</div>
      <div class="abs" style="left:98px;top:26px;font-size:5.5px;font-weight:600">General Manager</div>
      <div class="abs" style="left:98px;top:41px;width:110px;font-size:5.3px;line-height:1.85;text-align:justify">Lorem ipsum dolor sit amet, consectetur adipiscing elit</div>
    </div>
    <div class="ft"><span class="brand">MARLOWE</span><span class="num">16</span></div>
  </section>

  <!-- 17 Team 2 -->
  <section class="slide">
    <div class="photo" role="img" aria-label="Glass office tower seen from below" style="left:43px;top:0;width:416px;height:139px;border-radius:0 0 10px 10px;background:linear-gradient(170deg,#dfe6ee,#8b9aae 55%,#5f6f86)"></div>
    <div class="card white-c" style="left:341px;top:122px;width:85px;height:35px;border-radius:18px">
      <svg class="abs" style="left:9px;top:9px;width:17px;height:17px;color:var(--blue)"><use href="#dot-icon"/></svg>
      <div class="abs" style="left:38px;top:10px;font-size:10px;font-weight:600">100K</div>
    </div>
    <div class="t" style="left:43px;top:169px">Grow Our Team<br><b>Faster With Us</b></div>
    <div class="p" style="left:43px;top:220px;width:175px;text-align:justify">Lorem ipsum dolor sit amet, consectetuer adipiscing elit. Maecenas porttitor congue massa. Fusce posuere, magna sed pulvinar ultricies, purus lectus.</div>
    <div class="abs" style="left:251px;top:169px;width:17px;height:17px;border-radius:50%;background:var(--blue);color:#fff;font-size:5.5px;font-weight:600;display:flex;align-items:center;justify-content:center">01</div>
    <div class="lbl" style="left:282px;top:168px">Description</div>
    <div class="p" style="left:282px;top:179px;width:175px">Lorem ipsum dolor sit amet, consectetuer adipiscing elit. Maecenas porttitor congue massa. Fusce posuere.</div>
    <div class="abs" style="left:251px;top:220px;width:17px;height:17px;border-radius:50%;background:var(--blue);color:#fff;font-size:5.5px;font-weight:600;display:flex;align-items:center;justify-content:center">02</div>
    <div class="lbl" style="left:282px;top:219px">Description</div>
    <div class="p" style="left:282px;top:230px;width:175px">Lorem ipsum dolor sit amet, consectetuer adipiscing elit. Maecenas porttitor congue massa. Fusce posuere.</div>
    <div class="ft"><span class="brand">MARLOWE</span><span class="num">17</span></div>
  </section>

  <!-- 18 Thank you -->
  <section class="slide blue">
    <div class="photo tint" role="img" aria-label="Handshake and city skyline under a blue overlay" style="inset:0"></div>
    <div class="hd" style="left:369px">Business Company</div>
    <div class="hd" style="left:464px">2026</div>
    <div class="abs on-blue" style="left:40px;top:62px;width:200px;font-size:14px;font-weight:500;line-height:1.2">Marlowe Stewardship Partners</div>
    <div class="t on-blue" style="left:40px;top:126px;font-size:36px;font-weight:700">Thank You!</div>
    <div class="abs on-blue" style="left:43px;top:172px;font-size:8.5px;font-weight:600">Business Presentation Template</div>
    <div class="abs" style="left:43px;top:199px;width:415px;height:1px;background:rgba(255,255,255,.5)"></div>
    <div class="p on-blue" style="left:43px;top:220px;width:220px;color:#fff">Lorem ipsum dolor sit amet, consectetuer adipiscing elit. Maecenas porttitor congue massa. Fusce posuere, magna sed pulvinar.</div>
    <div class="btn light" style="left:384px;top:222px;width:74px">Learn More <svg><use href="#go-b"/></svg></div>
  </section>

</main>
</body>
</html>
```